Brolvane Tours - Astronomy in the Kimberley

Brolvane Tours requires a web page to advertise astronomy tours in the East Kimberley, Australia. It needs the following tabs - Home, Tours, Astronomy Events, Gallery, Testimonials, Contacts.

It should target tourists to the Kimberley.
We are unsure of which colours to go with at the moment but we have included our logo if it helps.

It should be mobile and tablet friendly.

Target Market(s)

Families, +40, Tourist, hobby astronomists,

Industry/Entity Type

Events

Number of Pages Required

3 page

Colors
3377b5
ffffff

Requirements
Must have
• Home, Tours, Astronomy Events, Gallery, Calendar, Testimonials, Contacts.
• 'Brolvane Tours' logo
Nice to have
• Pictures of portable amateur telescopes. Pictures of Lake Kununurra or Wyndham.
Should not have
• Pictures of extremely large professional telescopes.

```html
<!DOCTYPE html>
<html lang="en">
<head>
<meta charset="utf-8">
<title>Brolvane Tours – Astronomy in the Kimberley</title>
<link rel="stylesheet" href="https://fonts.googleapis.com/css2?family=Open+Sans:wght@300;400;600&display=swap">
<style>
:root{
  --blue:#3387c4;
  --blue-soft:#4e9fd1;
  --cream:#fcfaf1;
  --grey-bg:#efefef;
  --ink:#3a3a3a;
  --ink-soft:#8a8a8a;
  --line:#e1e1e1;
  --white:#ffffff;
}
*{box-sizing:border-box;margin:0;padding:0}
html,body{width:1200px;height:2395px;overflow:hidden}
body{font-family:"Open Sans",Arial,sans-serif;color:var(--ink);background:var(--cream);position:relative}

/* header */
.site-header{position:absolute;top:0;left:0;width:1200px;height:89px;background:var(--cream)}
.brand{position:absolute;left:106px;top:22px;display:flex;align-items:center;gap:10px;font-size:22px;font-weight:600;color:var(--blue)}
.brand-dot{width:20px;height:20px;border-radius:50%;background:var(--blue)}
.main-nav{position:absolute;left:555px;top:0;height:89px;display:flex}
.main-nav a{display:flex;align-items:center;height:89px;padding:0 13px;font-size:15px;color:var(--blue);text-decoration:none}
.main-nav a.active{background:var(--blue);color:var(--white);padding:0 16px}

/* hero */
.hero{position:absolute;top:89px;left:0;width:1200px;height:525px;
  background:linear-gradient(180deg,#6f9cc9 0%,#a9b9c9 28%,#c98a55 48%,#6b4a33 62%,#2e3f4f 78%,#1d2e3c 100%)}
.hero-icons{position:absolute;left:178px;top:320px;width:844px;height:44px}
.search-box{position:absolute;left:178px;top:370px;width:844px;height:83px;background:rgba(255,255,255,.85);padding:10px 14px}
.search-title{font-size:19px;color:#222;margin-bottom:8px}
.search-row{display:flex;height:32px;background:#f6f6f6;border:1px solid #e2e2e2;font-size:12px}
.search-row .field{display:flex;align-items:center;gap:6px;padding:0 8px;border-right:1px solid #e2e2e2;color:var(--blue);font-weight:600}
.search-row .field span{color:#b3b3b3;font-weight:400}
.f-from{width:150px}.f-to{width:174px}.f-dep{width:148px}.f-ret{width:130px}.f-adults{width:112px}
.search-btn{margin-left:auto;width:98px;background:var(--blue);color:var(--white);display:flex;align-items:center;justify-content:center;gap:8px;font-size:14px}
.hero-arrows{position:absolute;right:20px;bottom:14px;display:flex;gap:10px}

/* hot sale */
.hot-sale{position:absolute;top:614px;left:0;width:1200px;height:92px;background:var(--cream)}
.hot-sale h2{position:absolute;left:86px;top:28px;font-size:24px;font-weight:600;color:#333}
.hot-sale h2 span{font-weight:400;color:#555}
.all-sales{position:absolute;left:972px;top:24px;width:139px;height:44px;border:1px solid #c9d9e4;display:flex;align-items:center;justify-content:center;gap:12px;font-size:11px;letter-spacing:1px;color:#333}

/* deals */
.deals{position:absolute;top:706px;left:0;width:1200px;height:935px;background:var(--grey-bg)}
.deal-grid{position:absolute;left:89px;top:21px;display:grid;grid-template-columns:repeat(4,250px);grid-template-rows:435px 435px;column-gap:7px;row-gap:9px}
.deal-card{background:var(--white);border:1px solid #dcdcdc;position:relative}
.deal-photo{height:252px;position:relative}
.deal-photo.notch::after{content:"";position:absolute;left:116px;bottom:0;border:9px solid transparent;border-bottom-color:var(--white)}
.deal-body{padding:16px 16px}
.deal-title{font-size:21px;color:#444;line-height:1.25}
.deal-sub{font-size:16px;color:var(--ink-soft);margin-top:3px}
.deal-price{margin-top:46px;font-size:16px;color:var(--ink-soft);line-height:1.6}
.deal-price b,.deal-price .night{font-weight:400;color:var(--blue-soft)}

/* confidence */
.confidence{position:absolute;top:1641px;left:0;width:1200px;height:444px;
  background:linear-gradient(180deg,#2f4024 0%,#435a32 35%,#2a3a26 70%,#1f2b22 100%)}
.confidence-list{position:absolute;left:84px;top:48px;width:514px;color:var(--white)}
.confidence-list h3{font-size:22px;font-weight:600;padding-bottom:14px;border-bottom:1px solid rgba(255,255,255,.5)}
.conf-item{display:flex;gap:12px;margin-top:18px;height:45px}
.conf-num{width:26px;height:26px;border:1px solid var(--white);display:flex;align-items:center;justify-content:center;font-size:14px;flex:none;margin-top:2px}
.conf-item h4{font-size:18px;font-weight:600;line-height:1.1}
.conf-item p{font-size:12.5px;margin-top:3px}
.newsletter{position:absolute;left:665px;top:17px;width:444px;height:404px;background:var(--white);padding:44px 16px 0 16px}
.newsletter h3{font-size:23px;font-weight:600;color:#444;padding:0 0 16px 7px;border-bottom:1px solid var(--line)}
.newsletter p{font-size:12.5px;color:#666;line-height:1.35;margin:30px 0 0 0}
.email-row{margin-top:32px;display:flex;height:45px;border:1px solid var(--line)}
.email-icon{width:60px;background:#d6d6d6;display:flex;align-items:center;justify-content:center}
.email-input{flex:1;display:flex;align-items:center;padding-left:10px;font-size:13px;font-style:italic;color:#aaa}
.email-btn{width:98px;border-left:1px solid var(--line);display:flex;align-items:center;justify-content:center;gap:8px;font-size:13px;color:#777}
.follow{font-size:23px;color:#333;margin-top:50px}
.social{display:flex;gap:11px;margin-top:12px}
.social span{width:44px;height:44px;border:1px solid var(--line);display:flex;align-items:center;justify-content:center}
.social span i{width:10px;height:10px;background:#555;display:block}

/* footer */
.site-footer{position:absolute;top:2085px;left:0;width:1200px;height:255px;background:var(--cream)}
.foot-col{position:absolute;top:22px;width:232px}
.foot-col h5{font-size:14px;font-weight:400;color:#222;margin-bottom:16px}
.foot-col p{font-size:11px;line-height:1.35;color:#9a9a9a}
.foot-col ul{list-style:none}
.foot-col li{font-size:11px;color:#9a9a9a;padding:6px 0;border-bottom:1px solid var(--line);line-height:1.3}
.foot-col li:first-child{padding-top:0}
.col-a{left:91px;width:196px}.col-b{left:350px;width:232px}.col-c{left:633px;width:200px}.col-d{left:876px;width:234px}
.copyright{position:absolute;top:2340px;left:0;width:1200px;height:55px;background:#eeeeee;display:flex;align-items:center;justify-content:center;font-size:12px;color:#333}
</style>
</head>
<body>

<header class="site-header">
  <div class="brand"><span class="brand-dot"></span>Brolvane Tours</div>
  <nav class="main-nav">
    <a class="active" href="#">Home</a>
    <a href="#">Tours</a>
    <a href="#">Astronomy</a>
    <a href="#">Events</a>
    <a href="#">Gallery</a>
    <a href="#">Testimonials</a>
    <a href="#">Contacts</a>
  </nav>
</header>

<section class="hero" role="img" aria-label="Lakeside resort with thatched roof lit at dusk, palm trees and reflecting pool">
  <svg class="hero-icons" viewBox="0 0 844 44" fill="#fff">
    <path d="M58 20 l14-3 6-12 4 0 -3 11 9 -2 3-4 3 0 -2 6 2 6 -3 0 -3-4 -9-2 3 11 -4 0 -6-12 -14-3z"/>
    <path d="M62 38 l6 6 6-6z" fill="#fff"/>
    <path d="M242 8h14v28h-14z M246 12h2v3h-2z M251 12h2v3h-2z M246 18h2v3h-2z M251 18h2v3h-2z M246 24h2v3h-2z M251 24h2v3h-2z" fill-rule="evenodd"/>
    <path d="M405 22 l4-8h20l4 8h3v10h-4v3h-4v-3h-18v3h-4v-3h-4v-10z M412 22h16l-3-6h-10z" fill-rule="evenodd"/>
    <path d="M578 14h22v20h-22z M584 14v-4h10v4h-2v-2h-6v2z M600 18h10v16h-10z"/>
    <path d="M756 34 l4-16 c-6-2-10 0-12 3 c2-6 8-8 13-6 c-2-4-7-5-10-3 c4-4 10-3 12 1 c2-4 8-5 11-1 c-4-1-7 0-9 3 c5-1 9 2 10 6 c-3-3-8-4-12-2 l-3 15z M748 36h30v2h-30z"/>
  </svg>
  <div class="search-box">
    <div class="search-title">Where would you like to go?</div>
    <div class="search-row">
      <div class="field f-from">Flight From: <span>Airport</span></div>
      <div class="field f-to">To <span>Country,Airport</span></div>
      <div class="field f-dep">Departing: <svg width="12" height="12" viewBox="0 0 12 12"><rect x="0.5" y="1.5" width="11" height="10" fill="none" stroke="#aaa"/><path d="M0 4.5h12M4 2v10M8 2v10M0 8h12" stroke="#aaa"/></svg></div>
      <div class="field f-ret">Returning <svg width="12" height="12" viewBox="0 0 12 12"><rect x="0.5" y="1.5" width="11" height="10" fill="none" stroke="#aaa"/><path d="M0 4.5h12M4 2v10M8 2v10M0 8h12" stroke="#aaa"/></svg></div>
      <div class="field f-adults">Adults <svg width="10" height="6" viewBox="0 0 10 6"><path d="M1 1l4 4 4-4" fill="none" stroke="#999"/></svg></div>
      <div class="search-btn">Search <svg width="14" height="14" viewBox="0 0 14 14"><circle cx="6" cy="6" r="4.3" fill="none" stroke="#fff" stroke-width="2"/><path d="M9 9l4 4" stroke="#fff" stroke-width="2.2"/></svg></div>
    </div>
  </div>
  <svg class="hero-arrows" width="34" height="14" viewBox="0 0 34 14"><path d="M7 2l-5 5 5 5M27 2l5 5-5 5" fill="none" stroke="#fff" stroke-width="1.6"/></svg>
</section>

<section class="hot-sale">
  <h2>Hot Sale Today: <span>Lake Kununurra,Wyndham</span></h2>
  <div class="all-sales">ALL SALES <svg width="22" height="10" viewBox="0 0 22 10"><path d="M0 5h20M16 1l4 4-4 4" fill="none" stroke="#3387c4" stroke-width="1.3"/></svg></div>
</section>

<section class="deals">
  <div class="deal-grid">
    <article class="deal-card">
      <div class="deal-photo" role="img" aria-label="Red rock outcrop reflected in a still river" style="background:linear-gradient(180deg,#8fb3d8 0%,#c9d7e3 25%,#9b5b3c 50%,#4e6a3b 70%,#3d4a44 100%)"></div>
      <div class="deal-body"><div class="deal-title">Lorem Ipsum simply</div><div class="deal-sub">Printing and typese</div><div class="deal-price">From <b>$269</b><br><span class="night">$175/night</span></div></div>
    </article>
    <article class="deal-card">
      <div class="deal-photo" role="img" aria-label="Blue lake with a jetty below distant ranges" style="background:linear-gradient(180deg,#b9cfe2 0%,#aa9b74 22%,#2f5fa6 40%,#1f4f98 65%,#6b7a45 100%)"></div>
      <div class="deal-body"><div class="deal-title">Lorem Ipsum simply</div><div class="deal-sub">Printing and typese</div><div class="deal-price">From <b>$269</b><br><span class="night">$175/night</span></div></div>
    </article>
    <article class="deal-card">
      <div class="deal-photo" role="img" aria-label="Resort swimming pool lined with palm trees" style="background:linear-gradient(180deg,#4f86cf 0%,#a9c3e2 30%,#5f7c48 55%,#e2e2da 70%,#3cb2d6 85%,#2598c4 100%)"></div>
      <div class="deal-body"><div class="deal-title">Lorem Ipsum simply</div><div class="deal-sub">Printing and typese</div><div class="deal-price">From <b>$269</b><br><span class="night">$175/night</span></div></div>
    </article>
    <article class="deal-card">
      <div class="deal-photo" role="img" aria-label="Hotel lobby lounge with chandelier and armchairs" style="background:linear-gradient(180deg,#c99a4a 0%,#e6c680 35%,#b48a52 60%,#8e7a4e 80%,#6c5a3c 100%)"></div>
      <div class="deal-body"><div class="deal-title">Lorem Ipsum simply</div><div class="deal-sub">Printing and typese</div><div class="deal-price">From <b>$269</b><br><span class="night">$175/night</span></div></div>
    </article>
    <article class="deal-card">
      <div class="deal-photo notch" role="img" aria-label="Sunlit sea bay with islands" style="background:linear-gradient(180deg,#3f7fc8 0%,#8ec0ea 35%,#d8ecf8 55%,#4f8fcf 80%,#2f6fb1 100%)"></div>
      <div class="deal-body"><div class="deal-title">Lorem Ipsum simply</div><div class="deal-sub">Printing and typese</div><div class="deal-price">From <b>$269</b><br><span class="night">$175/night</span></div></div>
    </article>
    <article class="deal-card">
      <div class="deal-photo notch" role="img" aria-label="Small boat on a green river lined with trees" style="background:linear-gradient(180deg,#3d5a28 0%,#5d7d36 35%,#2f4a2a 60%,#406a48 80%,#2c4a36 100%)"></div>
      <div class="deal-body"><div class="deal-title">Lorem Ipsum simply</div><div class="deal-sub">Printing and typese</div><div class="deal-price">From <b>$269</b><br><span class="night">$175/night</span></div></div>
    </article>
    <article class="deal-card">
      <div class="deal-photo notch" role="img" aria-label="Guests seated by a lake at sunset" style="background:linear-gradient(180deg,#b7c2cf 0%,#d9c9c0 30%,#c2b2a8 50%,#6e6a4e 75%,#4a4636 100%)"></div>
      <div class="deal-body"><div class="deal-title">Lorem Ipsum simply</div><div class="deal-sub">Printing and typese</div><div class="deal-price">From <b>$269</b><br><span class="night">$175/night</span></div></div>
    </article>
    <article class="deal-card">
      <div class="deal-photo notch" role="img" aria-label="Lakeside camping ground on green lawn" style="background:linear-gradient(180deg,#c9d7e3 0%,#3f6fb0 15%,#4e6e3a 30%,#6f9a48 60%,#4d7a34 100%)"></div>
      <div class="deal-body"><div class="deal-title">Lorem Ipsum simply</div><div class="deal-sub">Printing and typese</div><div class="deal-price">From <b>$269</b><br><span class="night">$175/night</span></div></div>
    </article>
  </div>
</section>

<section class="confidence" role="img" aria-label="Dense green rainforest around a quiet creek">
  <div class="confidence-list">
    <h3>Book with confidence</h3>
    <div class="conf-item"><div class="conf-num">1</div><div><h4>No booking charges</h4><p>We don't charge you an extra fee for booking a hotel room with us</p></div></div>
    <div class="conf-item"><div class="conf-num">2</div><div><h4>No cancellation fees</h4><p>We don't charge you a cancellation or modification fee in case plans change</p></div></div>
    <div class="conf-item"><div class="conf-num">3</div><div><h4>Instant confirmation</h4><p>Instant booking confirmation whether booking online or via the telephone</p></div></div>
    <div class="conf-item"><div class="conf-num">4</div><div><h4>Flexible booking</h4><p>You can book up to a whole year in advance until the moment of your stay</p></div></div>
  </div>
  <div class="newsletter">
    <h3>Subscribe To Our Newsletter</h3>
    <p>Lorem Ipsum is simply dummy text of the printing and typeset ting industry. Lorem Ipsum has been the industry's stan dard dummy text ever since the</p>
    <div class="email-row">
      <div class="email-icon"><svg width="38" height="26" viewBox="0 0 38 26"><rect x="0.5" y="0.5" width="37" height="25" fill="#fff"/><path d="M1 1l18 14 18-14M1 25l13-12M37 25l-13-12" fill="none" stroke="#bbb"/></svg></div>
      <div class="email-input">Your Email</div>
      <div class="email-btn">Subcribe <svg width="8" height="14" viewBox="0 0 8 14"><path d="M1 1l6 6-6 6" fill="none" stroke="#3387c4" stroke-width="1.5"/></svg></div>
    </div>
    <div class="follow">Follow Us</div>
    <div class="social">
      <span aria-label="Social link 1"><i></i></span>
      <span aria-label="Social link 2"><i></i></span>
      <span aria-label="Social link 3"><i></i></span>
      <span aria-label="Social link 4"><i></i></span>
      <span aria-label="Social link 5"><i></i></span>
      <span aria-label="Social link 6"><i></i></span>
    </div>
  </div>
</section>

<footer class="site-footer">
  <div class="foot-col col-a">
    <h5>CORVENA</h5>
    <p>Lorem Ipsum is simply dummy text of the printing and typesetting industry. Lorem Ipsum has been the industry's standard dummy text ever since the 1500s, when an unknown printer took a galley of type and scrambled it to make a type specimen book. It has survived not only five centuries.</p>
  </div>
  <div class="foot-col col-b">
    <h5>META</h5>
    <ul><li>Lorem Ipsum is</li><li>Standard dummy text</li><li>Many desktop publish</li><li>Uncover many web sites</li></ul>
  </div>
  <div class="foot-col col-c">
    <h5>ARCHIVES</h5>
    <ul><li>Ferbuary 2015</li></ul>
  </div>
  <div class="foot-col col-d">
    <h5>RECENT POSTS</h5>
    <ul>
      <li>Lorem Ipsum is simply dummy<br>text of the printing</li>
      <li>Lorem Ipsum is simply dummy<br>text of the printing</li>
      <li>Lorem Ipsum is simply dummy<br>text of the printing</li>
      <li>Lorem Ipsum is simply dummy<br>text of the printing</li>
    </ul>
  </div>
</footer>
<div class="copyright">© 2015 Brolvane Tours All rights reserved.</div>

</body>
</html>
```